Home loan company

looking for a simple and professional looking website. Front page will have a map of Australia with several counters. Need to. Be able to register interest name ,contact, dollar amount ect. This info must be placed into a data base .

We have a logo , colour scheme and an in depth outline that will be sent to interested People.

Industry/Entity Type

Loan

Number of Pages Required

5+ page

```html
<!DOCTYPE html>
<html lang="en">
<head>
<meta charset="utf-8">
<title>Harbourline Home Loan</title>
<link href="https://fonts.googleapis.com/css2?family=Open+Sans:ital,wght@0,400;0,600;1,400&family=Raleway:wght@500;600&display=swap" rel="stylesheet">
<style>
  :root{
    --green:#1f9a57;
    --ink:#ffffff;
    --ink-muted:#d4d4d4;
    --ink-faint:#8d8d8d;
    --bg:#1c1c1c;
    --panel:#464646;
    --field:#3a3a3a;
    --field-border:#575757;
    --track:#6c6c6c;
    --radio:#6a6a6a;
    --rule:#7a7a7a;
    --footer:#3e3e3e;
    --map:#7d7d7d;
    --map-edge:#6f6f6f;
  }
  *{box-sizing:border-box;margin:0;padding:0}
  html,body{width:1200px;height:795px;overflow:hidden;background:var(--bg)}
  body{position:relative;font-family:"Open Sans",Arial,sans-serif;color:var(--ink)}

  .hero-photo{
    position:absolute;left:0;top:0;width:1200px;height:720px;
    background:
      radial-gradient(ellipse 340px 260px at 700px 300px,#4a4737 0%,rgba(60,58,48,.6) 45%,rgba(28,28,28,0) 100%),
      radial-gradient(ellipse 420px 180px at 690px 600px,#3a2e27 0%,rgba(40,32,28,.5) 50%,rgba(28,28,28,0) 100%),
      linear-gradient(180deg,#242424 0%,#1d1d1d 100%);
  }

  .brand{position:absolute;left:52px;top:45px;display:flex;align-items:flex-start;gap:14px}
  .brand-mark{width:38px;height:38px;background:var(--green);margin-top:4px}
  .brand-name{font-family:"Raleway",Arial,sans-serif;font-weight:600;font-size:24px;line-height:29px;color:var(--green);text-transform:uppercase}
  .brand-tagline{position:absolute;left:54px;top:129px;font-family:"Raleway",Arial,sans-serif;font-weight:500;font-size:9.5px;letter-spacing:1.6px;color:var(--ink-faint);text-transform:uppercase}

  .register-prompt{position:absolute;right:53px;top:43px;font-style:italic;font-size:17px;color:var(--ink)}
  .apply-button{position:absolute;left:913px;top:83px;width:234px;height:46px;border:1px solid var(--green);display:flex;align-items:center;justify-content:center;font-family:"Raleway",Arial,sans-serif;font-weight:500;font-size:21px;letter-spacing:.5px;color:var(--green);text-decoration:none;text-transform:uppercase}

  .loan-panel{position:absolute;left:52px;top:188px;width:357px;height:488px;background:var(--panel);padding:26px 28px 0 28px}
  .loan-panel h2{font-family:"Raleway",Arial,sans-serif;font-weight:600;font-size:17px;letter-spacing:.6px;text-transform:uppercase;padding-bottom:15px;border-bottom:2px solid var(--rule)}
  .field-label{position:absolute;left:28px;font-size:14px;color:var(--ink)}
  .slider{position:absolute;left:28px;width:150px;height:4px;border-radius:2px;background:var(--track)}
  .slider-thumb{position:absolute;top:-8px;width:10px;height:20px;border-radius:5px;background:var(--green)}
  .value-box{position:absolute;height:38px;background:var(--field);border:1px solid var(--field-border);font-size:13px;display:flex;align-items:center;padding-left:11px}
  .unit{position:absolute;font-size:13px}
  .radio-row{position:absolute;left:28px;display:flex;gap:15px;font-size:13px}
  .radio{display:flex;align-items:center;gap:9px}
  .radio::before{content:"";width:19px;height:19px;border-radius:50%;background:var(--radio)}
  .radio.is-selected::before{background:radial-gradient(circle,var(--green) 0 5px,var(--radio) 5.5px)}

  .state-map{
    position:absolute;left:445px;top:253px;width:367px;height:338px;
    border-radius:26px;
    background:linear-gradient(160deg,var(--map) 0%,var(--map-edge) 100%);
  }
  .state-label{position:absolute;transform:translate(-50%,-50%);font-family:"Raleway",Arial,sans-serif;font-weight:600;font-size:14px;color:var(--ink)}

  .team-divider{position:absolute;left:870px;top:234px;width:1px;height:362px;background:var(--rule)}
  .team-pointer{position:absolute;left:853px;top:407px}
  .team-list{position:absolute;left:918px;top:233px;list-style:none}
  .team{height:56.25px;font-size:13px;line-height:22px}
  .team-name{color:var(--green);font-weight:600}
  .team-count em{font-style:italic}

  .site-footer{position:absolute;left:0;top:720px;width:1200px;height:75px;background:var(--footer);display:flex;align-items:center;justify-content:space-between;padding:0 53px 0 54px;font-size:13px;color:var(--ink-muted)}
  .award{display:flex;align-items:center;gap:17px}
  .award-badge{width:40px;height:42px;background:#e6e6e6}
</style>
</head>
<body>
  <div class="hero-photo" role="img" aria-label="Photograph of hands holding a small model house, darkened as a background"></div>

  <header>
    <div class="brand">
      <span class="brand-mark"></span>
      <span class="brand-name">Harbourline<br>Home Loan</span>
    </div>
    <p class="brand-tagline">Turning lending upside down</p>
    <p class="register-prompt">interested to register?</p>
    <a class="apply-button" href="#apply">Apply online</a>
  </header>

  <section class="loan-panel">
    <h2>My Home Loan</h2>

    <span class="field-label" style="top:77px">Loan Amount</span>
    <div class="slider" style="top:128px"><span class="slider-thumb" style="left:12px"></span></div>
    <div class="value-box" style="left:207px;top:111px;width:123px">$ 300,000</div>

    <span class="field-label" style="top:161px">Loan Period</span>
    <div class="slider" style="top:212px"><span class="slider-thumb" style="left:117px"></span></div>
    <div class="value-box" style="left:207px;top:195px;width:48px">25</div>
    <span class="unit" style="left:264px;top:204px">years</span>

    <span class="field-label" style="top:245px">Interest Rate</span>
    <div class="slider" style="top:296px"><span class="slider-thumb" style="left:40px"></span></div>
    <div class="value-box" style="left:207px;top:279px;width:66px">6.25</div>
    <span class="unit" style="left:282px;top:288px">% p.a.</span>

    <span class="field-label" style="top:330px">Repayment Frequency</span>
    <div class="radio-row" style="top:364px">
      <span class="radio is-selected">Monthly</span>
      <span class="radio">Frequently</span>
      <span class="radio">Weekly</span>
    </div>

    <span class="field-label" style="top:397px">Repayment Type</span>
    <div class="radio-row" style="top:431px">
      <span class="radio is-selected">Principal &amp; interest</span>
      <span class="radio" style="margin-left:5px">Interest based</span>
    </div>
  </section>

  <div class="state-map" role="img" aria-label="Map of Australia divided into states and territories: WA, NT, SA, QLD, NSW, ACT, VIC and TAS"></div>
  <span class="state-label" style="left:523px;top:410px">WA</span>
  <span class="state-label" style="left:632px;top:353px">NT</span>
  <span class="state-label" style="left:735px;top:382px">QLD</span>
  <span class="state-label" style="left:646px;top:439px">SA</span>
  <span class="state-label" style="left:731px;top:467px">NSW</span>
  <span class="state-label" style="left:754px;top:490px">ACT</span>
  <span class="state-label" style="left:722px;top:527px">VIC</span>
  <span class="state-label" style="left:732px;top:577px">TAS</span>

  <span class="team-divider"></span>
  <svg class="team-pointer" width="18" height="30" viewBox="0 0 18 30" aria-hidden="true">
    <path d="M17 0 L1 15 L17 30" fill="none" stroke="#7a7a7a" stroke-width="1"/>
  </svg>

  <ul class="team-list">
    <li class="team"><span class="team-name">Team NSW</span> ($200,000,000.00)<br><span class="team-count">9560 <em>People registered</em></span></li>
    <li class="team"><span class="team-name">Team QLD</span> ($200,000,000.00)<br><span class="team-count">9560 <em>People registered</em></span></li>
    <li class="team"><span class="team-name">Team WA</span> ($200,000,000.00)<br><span class="team-count">9560 <em>People registered</em></span></li>
    <li class="team"><span class="team-name">Team SA</span> ($200,000,000.00)<br><span class="team-count">9560 <em>People registered</em></span></li>
    <li class="team"><span class="team-name">Team NT</span> ($200,000,000.00)<br><span class="team-count">9560 <em>People registered</em></span></li>
    <li class="team"><span class="team-name">Team VIC</span> ($200,000,000.00)<br><span class="team-count">9560 <em>People registered</em></span></li>
    <li class="team"><span class="team-name">Team TAS</span> ($200,000,000.00)<br><span class="team-count">9560 <em>People registered</em></span></li>
  </ul>

  <footer class="site-footer">
    <span>Copyright (c) 2015 Harbourline</span>
    <span class="award"><span class="award-badge"></span>Best Customer Satisfaction in the US</span>
  </footer>
</body>
</html>
```